VistaLume webpage - Design only no coding required

Please refer to "web content" uploaded 23rd Sep for content

We are a digital signage company based in Jakarta, Indonesia.

Our core business is placement of LCD Tv's in waiting rooms of various hospitals in Indonesia which plays educational videos regarding various health topics (prescription/ethical medicines), OTC drugs TVC and other FMCG and ads.

Our client portfolio consists of the worlds biggest and well known Pharmaceutical companies and also local pharmaceutical companies.

Other parts of our business are as follows:
- Patient symposiums
- Booths for product activation
- Queuing systems that we have developed in house that use an android tablet and connect to our TV's
- Branding. eg. Lift doors, banners (static signage)
- Hospital management software. Specially developed software that comes in a generic format and needs to be customized to suit each hospital. It manages everything for phone/web booking, queues, registration, patient records, doctors schedules, referrals, pharmacy and inventory and checkout/payments.

We are after a website redesign that is visually attractive and modern as we also deal with many advertising agencies.

Our logo is orange and black, however the black & white can be reversed if necessary.

Pages will need to be available in English & Bahasa Indonesia language formats.

I am happy to answer any questions asap, i can be contacted at info@vistalume.example.id

current site (www.vistalume.example.id)

Target Market(s)

Mainly our business is B2B dealing with advertising clients either directly or through ad agencies.

The other aspect of our target market is hospitals where we place our screens.

There is (but not largely) and consumer audience.

In summary:
We have the following target markets:
1. Advertisers/ad agencies
2. Hospitals that wish to use our business model to display content to their patients 3. We are in a developing country however most of our viewers and clients are from a high demographic profile

Industry/Entity Type

Pharmaceutical

Requirements
Must have
• We will require duplicates of the pages in English & Bahasa Indonesia

I would like the initial designs with a focus on being clean yet bold and emphasis on typography.

The following pages will be required (but not limited to) to qualify for the prize:

-Home

- About Us

- Services
(sub pages)
=Digital Signage
=Video Content Production
=Hospital Branding
=Event Management
=Seminar
=Queue System
=Hospital Management Software

-Why Choose Us?

- Contact Us

- Clients & Partners

- Gallery

Based on the "Nice to haves" site examples we do not necessarily require pictures of our LCD's/content on the main page(s) and would be happy to purchase required stock photos if needed/agreed.

We definitely want a modern feel and do not wish to overload with too much info on the main page.

(Please note the text in the attached file will most likely be changed once we have a design concept, probably less text)

Webpages we like:
http://www.brinklanternstudio.example/
http://quillharbor.example

Nice to have
• This is some of the international players which we want our site to look like:
www.pardelsign.example.au
http://www.morvexpanel.example.uk/
www.tallowgrid.example/

Should not have
• We prefer not to have old outdated fonts and a website that resembles anything like the current one, we are after a modern and professional feel.
These are some of our relative competitors of which we DO NOT want our website looking like but as a reference:
http://curabyte-global.example/index.html
http://zrk.example.id/

```html
<!DOCTYPE html>
<html lang="en">
<head>
<meta charset="utf-8">
<title>VistaLume Digital Signage</title>
<link href="https://fonts.googleapis.com/css2?family=Open+Sans:wght@400;600;700&family=Cinzel:wght@400;700&display=swap" rel="stylesheet">
<style>
:root{
  --orange:#f2a71b;
  --orange-dark:#d98a0c;
  --orange-deep:#c9790a;
  --ink:#1b1b1b;
  --charcoal:#2a2a2a;
  --slate:#333;
  --grey:#9a9a9a;
  --light:#f4f4f4;
  --white:#fff;
}
*{box-sizing:border-box;margin:0;padding:0}
html,body{width:1200px;height:2872px;overflow:hidden}
body{font-family:"Open Sans",Arial,sans-serif;color:var(--ink);background:var(--white)}
section,header,footer{position:relative;width:1200px;overflow:hidden}
.serif{font-family:"Cinzel",Georgia,serif}

/* hero */
.hero{height:690px;background:linear-gradient(180deg,#5a4126 0%,#3d2e20 30%,#2a221b 52%,#1d1b1a 72%,#202020 100%)}
.hero-photo{position:absolute;inset:0;background:radial-gradient(ellipse at 55% 25%,rgba(214,160,90,.45),rgba(0,0,0,0) 60%)}
.topbar{position:absolute;top:0;left:0;right:0;height:78px;background:rgba(20,16,12,.7)}
.brand{position:absolute;left:30px;top:22px;display:flex;align-items:center;gap:10px;color:var(--white);font-weight:700;font-size:26px}
.brand i{width:22px;height:22px;border-radius:50%;background:var(--orange);display:block}
.nav{position:absolute;left:510px;top:24px;display:flex;gap:8px;list-style:none}
.nav li{font-size:15px;color:var(--white);padding:6px 14px}
.nav li.active{background:var(--orange);color:var(--ink);font-weight:600}
.hero-title{position:absolute;top:100px;left:0;right:0;text-align:center;color:var(--white)}
.hero-title small{display:block;font-size:18px;margin-bottom:2px}
.hero-title h1{font-size:50px;font-weight:700;line-height:1.05;text-shadow:0 2px 6px rgba(0,0,0,.5)}
.hero-intro{position:absolute;top:262px;left:370px;width:500px;color:var(--white);font-size:18px;line-height:1.35;text-align:center}
.features{position:absolute;top:392px;left:0;right:0}
.feature{position:absolute;width:176px;text-align:center;transform:translateX(-50%)}
.feature .disc{width:168px;height:168px;border-radius:50%;border:5px solid var(--white);margin:0 auto;box-shadow:0 4px 12px rgba(0,0,0,.5)}
.feature p{margin-top:30px;font-size:13px;line-height:1.4;color:var(--white);padding:0 4px}
.feature p em{font-style:normal;color:var(--orange)}

/* about teaser */
.teaser{height:400px;background:linear-gradient(180deg,var(--orange) 0%,#e89a12 100%);text-align:center;color:var(--white)}
.teaser small{display:block;padding-top:44px;font-size:16px}
.teaser h2{font-size:40px;font-weight:700;margin-top:2px}
.teaser p{width:880px;margin:40px auto 0;font-size:18px;line-height:1.7}
.btn{display:inline-block;font-size:13px;font-weight:600;letter-spacing:.5px;padding:12px 22px;color:var(--white)}
.teaser .actions{margin-top:30px;display:flex;justify-content:center;gap:70px}
.teaser .btn{background:var(--orange-deep)}

/* about */
.about{height:440px;background:var(--white)}
.about h2{text-align:center;padding-top:80px;font-size:40px;font-weight:400;color:var(--charcoal)}
.about-photo{position:absolute;left:148px;top:158px;width:224px;height:172px;background:linear-gradient(135deg,#8a6a4a,#3e3025 60%,#6b5440);border:4px solid #eee}
.about-text{position:absolute;left:412px;top:152px;width:668px;font-size:13.5px;line-height:1.62;color:#555}
.about .btn{position:absolute;left:960px;top:358px;background:var(--orange)}

/* why */
.why{height:420px;background:var(--charcoal);text-align:center}
.why h2{padding-top:70px;font-size:36px;color:var(--orange);font-weight:700}
.why-text{width:820px;margin:22px auto 0;font-size:13.5px;line-height:1.55;color:#cfcfcf}
.why-text .hl{color:var(--orange)}
.why .btn{margin-top:22px;background:var(--orange)}

/* services */
.services{height:350px;background:linear-gradient(180deg,#151c26 0%,#2b2a2c 45%,#3a2a1c 100%)}
.services h2{text-align:center;padding-top:58px;font-size:34px;color:var(--orange)}
.service{position:absolute;top:150px;width:170px;text-align:center;transform:translateX(-50%)}
.service .disc{width:144px;height:144px;border-radius:50%;border:4px solid var(--white);margin:0 auto}
.service span{display:block;margin-top:14px;font-size:15px;color:var(--white);line-height:1.25}
.arrow{position:absolute;top:204px;width:40px;height:40px;border-radius:50%;background:rgba(255,255,255,.25)}

/* partners */
.partners{height:160px;background:var(--white)}
.partner{position:absolute;top:50px;height:60px;background:#e2e2e2}

/* footer */
.footer{height:360px;background:var(--slate);color:#ccc;font-size:13px}
.col{position:absolute;top:34px}
.col h4{color:var(--white);font-size:16px;font-weight:600;border-bottom:1px solid #555;padding-bottom:8px;margin-bottom:16px}
.contact{left:160px;width:300px}
.inputs{display:flex;gap:10px}
.field{background:var(--white);height:30px;flex:1;color:#999;font-size:12px;padding:7px 8px}
.message{background:var(--white);height:150px;margin-top:10px;color:#999;font-size:12px;padding:7px 8px}
.form-actions{margin-top:12px;display:flex;gap:10px}
.form-actions .btn{background:var(--orange);padding:7px 20px;font-size:12px}
.location{left:520px;width:280px}
.location li{list-style:none;display:flex;gap:10px;margin-bottom:12px;line-height:1.5}
.location svg{flex:none;margin-top:2px}
.navigation{left:860px;width:220px}
.navigation ul{list-style:none;display:grid;grid-template-columns:1fr 1fr;row-gap:12px}
.navigation li::before{content:"› ";color:var(--orange)}
.copyright{height:52px;background:#1c1c1c;color:#9a9a9a;font-size:12px;padding:18px 160px}
</style>
</head>
<body>

<header class="hero">
  <div class="hero-photo" role="img" aria-label="Blurred photograph of a hospital waiting room with a digital screen"></div>
  <div class="topbar">
    <div class="brand"><i></i>VistaLume</div>
    <ul class="nav">
      <li class="active">Home</li><li>About us</li><li>Services</li><li>Why Choose us</li><li>Gallery</li><li>Contact us</li>
    </ul>
  </div>
  <div class="hero-title">
    <small>Welcome to</small>
    <h1>VistaLume Digital<br>Signage</h1>
  </div>
  <p class="hero-intro">Introduction sentence goes here - lorem ipsum dolor sit amet consectetur adipiscing elit. Integer euismod quis mauris quis</p>
  <div class="features">
    <div class="feature" style="left:288px"><div class="disc" role="img" aria-label="Photo of the team at a product activation booth" style="background:linear-gradient(135deg,#c9b79a,#6d5a48)"></div><p>We provide <em>streamlined access</em> for marketing within <em>Hospitals</em></p></div>
    <div class="feature" style="left:472px"><div class="disc" role="img" aria-label="Dark panel with the company emblem" style="background:#111"></div><p><em>Sentence goes here</em> and adds your value</p></div>
    <div class="feature" style="left:660px"><div class="disc" role="img" aria-label="Illustration of a help and challenge concept" style="background:linear-gradient(135deg,#f3f3f3,#bdbdbd)"></div><p>We <em>simply love</em> a challenge, we do more than digital signage</p></div>
    <div class="feature" style="left:852px"><div class="disc" role="img" aria-label="Photo of a screen in a hospital waiting room" style="background:linear-gradient(135deg,#8aa3b4,#3f4d58)"></div><p>We provide <em>LED screens</em> in hospital waiting rooms for <em>patient viewing</em></p></div>
  </div>
</header>

<section class="teaser">
  <small>A little</small>
  <h2 class="serif">About VistaLume</h2>
  <p>VistaLume was established to facilitate direct to customer marketing opportunities, especially within the healthcare system. Our digital signage system uses the latest technology &amp; software to deliver reliable &amp; effective content to its viewers in a highly segmented manner</p>
  <div class="actions"><span class="btn">LEARN MORE</span><span class="btn">GET IN TOUCH</span></div>
</section>

<section class="about">
  <h2 class="serif">About us</h2>
  <div class="about-photo" role="img" aria-label="Photo of a seminar audience in a meeting room"></div>
  <p class="about-text">PT VistaLume was founded not only as a business, but with the philosophy that we can make a difference in our audience, especially those visiting healthcare establishments such as Hospitals in Indonesia. We have a highly dedicated team who eat, breathe and sleep with the same philosophy. From the grassroots foundation, VistaLume identifies the segment of high income and educated viewers who visit the hospitals. This audience is ideal for advertisers because it can be efficiently reached by very few other media. It is therefore our aim to provide information that is relevant, clear and useful to every visitor. Our mission is to work with known hospital groups and industry leaders, delivering the right message at the right moment, and to build a trusted screen network that grows with our partners and clients across the country.</p>
  <span class="btn">READ MORE</span>
</section>

<section class="why">
  <h2 class="serif">Why Choose Us?</h2>
  <div class="why-text">
    <p>VistaLume has always taken a customer centric approach. Before establishing our business we spent much time with various Pharmaceutical companies, Hospitals &amp; Doctors to understand the market and the best mode of entry.</p>
    <p>Until today nothing much has changed. We always listen to what our clients want and think of unique and effective ways to satisfy their requirements.</p>
    <p class="hl">Efficient execution and exceptional service is paramount to our business philosophy, why wouldn't you choose us?</p>
    <p>Areas of specialization:</p>
    <p>Digital Signage – Queue management systems – Hospital branding – Video production – Event management – Hospital management software – Marketing placement</p>
  </div>
  <span class="btn">CLICK HERE FOR MORE INFORMATION</span>
</section>

<section class="services" role="img" aria-label="Night city traffic photograph behind the services list">
  <h2 class="serif">Services we Provide</h2>
  <span class="arrow" style="left:24px"></span>
  <span class="arrow" style="left:1136px"></span>
  <div class="service" style="left:252px"><div class="disc" role="img" aria-label="Screen in a waiting room" style="background:linear-gradient(135deg,#9db0bd,#40505a)"></div><span>Digital Signage</span></div>
  <div class="service" style="left:440px"><div class="disc" role="img" aria-label="Video production studio" style="background:linear-gradient(135deg,#5c6f86,#1f2a38)"></div><span>Content Video<br>Production</span></div>
  <div class="service" style="left:620px"><div class="disc" role="img" aria-label="Branded hospital lift doors" style="background:linear-gradient(135deg,#e0c07a,#8a6a2a)"></div><span style="color:var(--orange)">Hospital Branding</span></div>
  <div class="service" style="left:800px"><div class="disc" role="img" aria-label="Product activation booth" style="background:linear-gradient(135deg,#b9c98a,#5a6e33)"></div><span>BTL Activation</span></div>
  <div class="service" style="left:972px"><div class="disc" role="img" aria-label="Queue management tablet" style="background:linear-gradient(135deg,#cfcfcf,#6b6b6b)"></div><span>Queue Management<br>System</span></div>
</section>

<section class="partners">
  <div class="partner" style="left:130px;width:60px;border-radius:50%"></div>
  <div class="partner" style="left:320px;width:80px"></div>
  <div class="partner" style="left:560px;width:180px"></div>
  <div class="partner" style="left:790px;width:150px;height:30px;top:65px"></div>
  <div class="partner" style="left:1000px;width:150px;height:30px;top:65px"></div>
</section>

<footer class="footer">
  <div class="col contact">
    <h4>Contact us</h4>
    <div class="inputs"><div class="field">Name</div><div class="field">Email</div></div>
    <div class="message">Message</div>
    <div class="form-actions"><span class="btn">SUBMIT</span><span class="btn">RESET</span></div>
  </div>
  <div class="col location">
    <h4>Location</h4>
    <ul>
      <li><svg width="12" height="16" viewBox="0 0 12 16"><path d="M6 0a6 6 0 0 0-6 6c0 4.5 6 10 6 10s6-5.5 6-10a6 6 0 0 0-6-6zm0 8.5A2.5 2.5 0 1 1 6 3.5a2.5 2.5 0 0 1 0 5z" fill="#f2a71b"/></svg><span>Gedung Arunika Lt. 7 Unit 704<br>Jl. Kenari Indah No. 21<br>Jakarta Timur</span></li>
      <li><svg width="14" height="14" viewBox="0 0 14 14"><path d="M3 0l2.5 3.5-1.5 2a8 8 0 0 0 4.5 4.5l2-1.5L14 11l-2 3C5.5 13.5.5 8.5 0 2z" fill="#f2a71b"/></svg><span>Phone : 021 - 5550 1234<br>Fax : 021 - 5550 1235</span></li>
    </ul>
  </div>
  <div class="col navigation">
    <h4>Navigation</h4>
    <ul><li>Home</li><li>Why choose us</li><li>About us</li><li>Gallery</li><li>Services</li><li>Contact us</li></ul>
  </div>
</footer>
<div class="copyright">© Copyright 2013 - VistaLume Digital Signage. All Rights Reserved.</div>

</body>
</html>
```